Brightfold Partners Website

Brightfold Partners Advisory Services is a company which provides specialised advise in carbon markets, climate policy, landscapes, resilience and change. We are based in Australia but the majority of our business is global. Our clients range from governments to large corporates and not for profit organisations.
Our focus is on developing the capabilities of government officials, business decision makers and land managers so they can better navigate the complexity of climate change and sustainability.
We are looking for a website that is consistent with the high end professional services which we provide to serious players.
I have attached two versions of our logo. I have also attached the back of our business card so you can get a sense of what we hand to potential clients.

Target Market(s)

Professional individuals, decision makers, board members etc, government officials.

Industry/Entity Type

Government

Number of Pages Required

4 page

Font styles to use
Serif
Sans Serif

Requirements
Must have
• Please provide
• 1. Home page
• 2. Service page template
• 3. Contact page
• 4. Lead expert profile page

```html
<!DOCTYPE html>
<html lang="en">
<head>
<meta charset="utf-8">
<title>Brightfold Partners Website</title>
<link href="https://fonts.googleapis.com/css2?family=Cinzel:wght@400;700&family=Open+Sans:wght@400;600;700&display=swap" rel="stylesheet">
<style>
:root{
  --ink:#2f3236;
  --dark:#2d3034;
  --dark-2:#3f4348;
  --text:#555a5f;
  --muted:#9a9ea2;
  --light:#f1f1f1;
  --line:#dcdcdc;
  --accent:#b7352c;
  --white:#ffffff;
}
*{box-sizing:border-box;margin:0;padding:0}
html,body{width:1200px;height:2304px;overflow:hidden;background:var(--white)}
body{font-family:"Open Sans",Arial,sans-serif;color:var(--text);position:relative}
.serif{font-family:"Cinzel",Georgia,serif}

.site-header{position:absolute;top:0;left:0;width:1200px;height:96px;background:var(--dark);display:flex;align-items:center;justify-content:space-between;padding:0 170px}
.brand{display:flex;align-items:center;gap:14px;color:var(--white)}
.brand-dot{width:46px;height:46px;border-radius:50%;background:var(--white)}
.brand-name{font-family:"Cinzel",Georgia,serif;font-size:22px;line-height:24px;letter-spacing:1px;font-weight:400}
.main-nav{display:flex;align-items:center;gap:30px}
.main-nav a{color:var(--white);text-decoration:none;font-size:13px;font-weight:600;letter-spacing:1px}
.social{display:flex;gap:12px;margin-left:10px}
.social span{width:12px;height:12px;border-radius:50%;background:#c9cbcd}

.hero{position:absolute;top:96px;left:0;width:1200px;height:444px;background:linear-gradient(100deg,#d9d3c8 0%,#efe9df 35%,#c9b9a2 65%,#8e7a63 100%)}
.hero-arrow{position:absolute;top:195px;width:46px;height:46px;border-radius:50%;border:2px solid rgba(255,255,255,.85);background:rgba(0,0,0,.25)}
.hero-arrow.prev{left:60px}
.hero-arrow.next{right:60px}
.hero-arrow svg{position:absolute;left:13px;top:13px}
.hero-panel{position:absolute;top:120px;left:890px;width:230px;padding:18px 16px;background:rgba(40,43,46,.88);color:var(--white)}
.hero-panel h2{font-family:"Cinzel",Georgia,serif;font-weight:400;font-size:30px;line-height:32px;letter-spacing:1px}
.hero-panel p{font-family:"Cinzel",Georgia,serif;font-size:14px;line-height:19px;margin-top:12px}
.btn-primary{position:absolute;top:268px;left:920px;width:150px;height:38px;background:var(--accent);color:var(--white);font-size:12px;font-weight:700;letter-spacing:1px;display:flex;align-items:center;justify-content:center}
.hero-dots{position:absolute;bottom:18px;left:575px;display:flex;gap:8px}
.hero-dots span{width:11px;height:11px;border-radius:50%;background:rgba(255,255,255,.6)}
.hero-dots span.on{background:var(--white)}

.info-strip{position:absolute;top:540px;left:0;width:1200px;height:40px;border-bottom:1px solid var(--line);display:flex;justify-content:space-between;align-items:center;padding:0 170px;font-size:11px;color:var(--muted)}
.info-strip span{display:flex;align-items:center;gap:8px}

.welcome{position:absolute;top:620px;left:0;width:1200px;text-align:center}
.welcome h1{font-family:"Cinzel",Georgia,serif;font-weight:400;font-size:36px;color:var(--ink);letter-spacing:1px}
.welcome p{font-size:13px;color:var(--text);margin-top:12px}
.welcome hr{width:300px;margin:10px auto 0;border:0;border-top:1px solid var(--line)}

.service-grid{position:absolute;top:720px;left:170px;width:860px;display:grid;grid-template-columns:422px 422px;column-gap:16px;row-gap:38px}
.service-card .media{height:238px}
.service-card h3{font-family:"Cinzel",Georgia,serif;font-weight:700;font-size:25px;color:var(--ink);margin-top:30px;letter-spacing:.5px}
.service-card p{font-size:12px;line-height:20px;color:var(--text);margin-top:8px;height:82px}
.btn-read{display:inline-block;margin-top:18px;background:var(--dark);color:var(--white);font-size:10px;font-weight:700;letter-spacing:1px;padding:7px 14px}
.media.carbon{background:linear-gradient(135deg,#1d1d1d,#4b4a48 55%,#9b8a6a)}
.media.climate{background:radial-gradient(circle at 50% 60%,#e08a2c,#b95a16 45%,#5a2b0c)}
.media.landscape{background:linear-gradient(180deg,#5a8fcf 0%,#a9c6e6 40%,#cfd8dc 55%,#4e7a3a 72%,#2f5a23 100%)}
.media.resilience{background:linear-gradient(180deg,#e7dfd2 0%,#c8b49a 55%,#8a6b4b 100%)}

.features{position:absolute;top:1765px;left:0;width:1200px;height:235px;background:var(--light);display:flex;justify-content:center;gap:60px;padding-top:38px}
.feature{width:250px;text-align:center}
.feature svg{display:block;margin:0 auto}
.feature h4{font-family:"Cinzel",Georgia,serif;font-weight:700;font-size:17px;color:var(--ink);margin-top:14px}
.feature p{font-size:11px;line-height:17px;color:var(--text);margin-top:8px}

.contact-band{position:absolute;top:2000px;left:0;width:1200px;height:180px;background:var(--dark)}
.contact-title{position:absolute;top:32px;left:0;width:1200px;display:flex;justify-content:center;align-items:center;gap:16px;color:var(--white)}
.contact-title .brand-dot{width:52px;height:52px}
.contact-title h2{font-family:"Cinzel",Georgia,serif;font-weight:400;font-size:34px;letter-spacing:1px}
.contact-form{position:absolute;top:118px;left:170px;width:860px;display:flex;gap:12px}
.field{height:36px;background:var(--dark-2);color:#b8bbbe;font-size:10px;font-weight:600;letter-spacing:1px;padding:0 14px;display:flex;align-items:center}
.field.name{width:300px}
.field.email{width:400px}
.btn-send{width:124px;height:36px;background:#e4e4e4;color:var(--ink);font-size:11px;font-weight:700;letter-spacing:1px;display:flex;align-items:center;justify-content:center}

.site-footer{position:absolute;top:2180px;left:0;width:1200px;height:124px;display:flex;align-items:center;justify-content:space-between;padding:0 170px;font-size:11px;color:var(--muted)}
.footer-mark{position:absolute;left:582px;top:44px;width:36px;height:36px;border-radius:50%;border:2px solid var(--muted)}
.site-footer .social span{width:18px;height:18px;background:#c6c8ca}
</style>
</head>
<body>

<header class="site-header">
  <div class="brand"><span class="brand-dot"></span><span class="brand-name">BRIGHTFOLD<br>PARTNERS</span></div>
  <nav class="main-nav">
    <a href="#">HOME</a><a href="#">SERVICES</a><a href="#">PROFILE</a><a href="#">CONTACT</a>
    <div class="social"><span></span><span></span><span></span><span></span></div>
  </nav>
</header>

<section class="hero" role="img" aria-label="Photo of two advisers meeting in a bright modern office lounge">
  <div class="hero-arrow prev"><svg width="20" height="20" viewBox="0 0 20 20"><path d="M13 3 L6 10 L13 17" fill="none" stroke="#fff" stroke-width="2.5"/></svg></div>
  <div class="hero-arrow next"><svg width="20" height="20" viewBox="0 0 20 20"><path d="M7 3 L14 10 L7 17" fill="none" stroke="#fff" stroke-width="2.5"/></svg></div>
  <div class="hero-panel">
    <h2>BRIGHTFOLD<br>PARTNERS</h2>
    <p>We are providing the best advisory services !</p>
  </div>
  <div class="btn-primary">GET REGISTER</div>
  <div class="hero-dots"><span class="on"></span><span></span><span></span></div>
</section>

<div class="info-strip">
  <span><svg width="12" height="12" viewBox="0 0 12 12"><path d="M2 1h3l1 3-1.5 1a7 7 0 0 0 2.5 2.5L8 6l3 1v3a1 1 0 0 1-1 1A9 9 0 0 1 1 2a1 1 0 0 1 1-1z" fill="#9a9ea2"/></svg>(02) 5550 1842</span>
  <span><svg width="14" height="10" viewBox="0 0 14 10"><rect x="0.5" y="0.5" width="13" height="9" fill="none" stroke="#9a9ea2"/><path d="M1 1l6 5 6-5" fill="none" stroke="#9a9ea2"/></svg>hello@brightfold.example</span>
</div>

<section class="welcome">
  <h1>WELCOME TO THE BRIGHTFOLD PARTNERS !</h1>
  <p>Brightfold Partners Advisory Services</p>
  <hr>
</section>

<section class="service-grid">
  <article class="service-card">
    <div class="media carbon" role="img" aria-label="Photo of a hand passing coal and banknotes"></div>
    <h3>CARBON MARKETS</h3>
    <p>We help governments and companies understand carbon markets, from offset standards and registries to trading strategy. Our advisers explain pricing, integrity and risk in plain terms so decision makers can act with confidence and build programs that hold up to scrutiny over time.</p>
    <span class="btn-read">READ MORE</span>
  </article>
  <article class="service-card">
    <div class="media climate" role="img" aria-label="Illustration of a glowing globe with industry around it"></div>
    <h3>CLIMATE POLICY</h3>
    <p>Climate policy moves quickly across jurisdictions. We track national and international frameworks, brief boards and officials on what changes mean for them, and support the design of policy that is practical, fair and ready to be delivered by the people who must carry it out.</p>
    <span class="btn-read">READ MORE</span>
  </article>
  <article class="service-card">
    <div class="media landscape" role="img" aria-label="Photo of green alpine meadows below snowy mountains"></div>
    <h3>LANDSCAPES</h3>
    <p>Land managers face new choices about soil, water, vegetation and income. We work alongside them to plan landscapes that store carbon, protect biodiversity and stay productive, bringing science, local knowledge and market opportunity together in one clear and workable plan.</p>
    <span class="btn-read">READ MORE</span>
  </article>
  <article class="service-card">
    <div class="media resilience" role="img" aria-label="Photo of a young seedling growing from cracked dry earth"></div>
    <h3>RESILIENCE</h3>
    <p>Resilience means being ready for shocks before they arrive. We assess climate risk across assets, supply chains and communities, then build the skills and systems organisations need to adapt, recover and keep serving the people who depend on them.</p>
    <span class="btn-read">READ MORE</span>
  </article>
</section>

<section class="features">
  <div class="feature">
    <svg width="50" height="50" viewBox="0 0 50 50"><circle cx="25" cy="20" r="11" fill="none" stroke="#2f3236" stroke-width="2"/><path d="M20 31v6h10v-6M21 41h8" fill="none" stroke="#2f3236" stroke-width="2"/><path d="M25 2v4M8 20h4M38 20h4M12 8l3 3M38 8l-3 3" stroke="#2f3236" stroke-width="2"/></svg>
    <h4>CREATIVE SOLUTIONS</h4>
    <p>Fresh thinking shaped around your goals, with practical options that suit your sector and scale.</p>
  </div>
  <div class="feature">
    <svg width="50" height="50" viewBox="0 0 50 50"><circle cx="25" cy="25" r="18" fill="none" stroke="#2f3236" stroke-width="2"/><circle cx="25" cy="25" r="7" fill="none" stroke="#2f3236" stroke-width="2"/><path d="M25 3v8M25 39v8M3 25h8M39 25h8" stroke="#2f3236" stroke-width="2"/></svg>
    <h4>FEATURED SERVICES</h4>
    <p>Advisory, training and research services for leaders working on climate and sustainability.</p>
  </div>
  <div class="feature">
    <svg width="50" height="50" viewBox="0 0 50 50"><circle cx="25" cy="25" r="14" fill="none" stroke="#2f3236" stroke-width="2"/><path d="M8 27v-4a17 17 0 0 1 34 0v4" fill="none" stroke="#2f3236" stroke-width="2"/><rect x="5" y="24" width="6" height="10" fill="#2f3236"/><rect x="39" y="24" width="6" height="10" fill="#2f3236"/></svg>
    <h4>TECHNICAL SUPPORT</h4>
    <p>Ongoing help from our team as you put plans into action and report on results.</p>
  </div>
</section>

<section class="contact-band">
  <div class="contact-title"><span class="brand-dot"></span><h2>CONTACT US NOW !</h2></div>
  <div class="contact-form">
    <div class="field name">NAME</div>
    <div class="field email">EMAIL</div>
    <div class="btn-send">SEND</div>
  </div>
</section>

<footer class="site-footer">
  <span>Brightfold Partners © 2014 Privacy Policy</span>
  <span class="footer-mark"></span>
  <div class="social"><span></span><span></span><span></span><span></span></div>
</footer>

</body>
</html>
```